Half-off Holiday Sale: Larkwood Academy

The online course called Larkwood Academy. Once a year, I run a 1/2 off special (expired Dec 31). You can see what the school is all about here: larkwood-academy.com and I'll attach a picture of the current ad we're running.
www.larkwood-academy.com

Please stick with the brain/puzzle logo as the theme, but make the 50% off appealing and inviting.

** I plan on paying for more than one design. I'd like to buy a few different ones!

Target Market(s)

People with Parkinson's disease and their families.

Industry/Entity Type

medical care/ education

Requirements
Must have
• LA School (Larkwood Academy) logo; Must say "50% off" or something like that.

```html
<!DOCTYPE html>
<html lang="en">
<head>
<meta charset="utf-8">
<title>Larkwood Academy – 50% off</title>
<link rel="stylesheet" href="https://fonts.googleapis.com/css2?family=Anton&family=Titillium+Web:wght@700&family=Arimo&display=swap">
<style>
  :root {
    --stage: #444444;
    --sun-core: #fff6b0;
    --sun-mid: #ffd21f;
    --sun-edge: #f7a41b;
    --paper: #ffffff;
    --brand-orange: #e54e1f;
    --brand-grey: #8d9592;
    --tagline: #666666;
    --numeral: #f4f4f4;
    --numeral-shade: #d6d6d6;
    --depth: #6a1d12;
    --gold-top: #ffe94a;
    --gold-bottom: #f59a17;
  }
  * { margin: 0; padding: 0; box-sizing: border-box; }
  html, body { width: 1200px; height: 1000px; overflow: hidden; background: var(--stage); }
  .canvas { position: relative; width: 1200px; height: 1000px; }
  .promo-card {
    position: absolute; left: 170px; top: 70px; width: 860px; height: 860px;
    background: radial-gradient(circle at 50% 50%, var(--sun-core) 0%, var(--sun-mid) 45%, var(--sun-edge) 100%);
    overflow: hidden;
  }
  .content-sheet {
    position: absolute; left: 45px; top: 128px; width: 770px; height: 687px;
    background: var(--paper);
  }
  .brand-dot {
    position: absolute; left: 340px; top: 40px; width: 162px; height: 188px;
    border-radius: 50%; background: var(--brand-orange); border: 4px solid var(--paper);
  }
  .brand {
    position: absolute; left: 0; top: 238px; width: 860px; text-align: center;
  }
  .brand-name {
    font-family: "Titillium Web", sans-serif; font-weight: 700;
    font-size: 56px; line-height: 1; letter-spacing: 1px;
    color: var(--brand-grey); margin-left: -10px;
  }
  .brand-tagline {
    font-family: "Arimo", sans-serif; font-size: 19px; line-height: 1.2; color: var(--tagline);
    margin-top: 10px; margin-left: -10px;
  }
  .offer-band { position: absolute; left: 0; top: 0; }
  .offer-text { font-family: "Anton", sans-serif; }
</style>
</head>
<body>
<div class="canvas">
  <div class="promo-card">
    <div class="content-sheet"></div>
    <div class="brand-dot"></div>
    <div class="brand">
      <div class="brand-name">LARKWOOD ACADEMY</div>
      <div class="brand-tagline">An Online Course for Patients and Providers</div>
    </div>
    <svg class="offer-band" width="860" height="860" viewBox="170 70 860 860" aria-label="50% off">
      <defs>
        <linearGradient id="numeral-fill" x1="0" y1="0" x2="0" y2="1">
          <stop offset="0" stop-color="var(--numeral)"/>
          <stop offset="1" stop-color="var(--numeral-shade)"/>
        </linearGradient>
        <linearGradient id="gold-fill" x1="0" y1="0" x2="0" y2="1">
          <stop offset="0" stop-color="var(--gold-top)"/>
          <stop offset="1" stop-color="var(--gold-bottom)"/>
        </linearGradient>
      </defs>
      <rect x="170" y="436" width="860" height="384" fill="var(--brand-orange)"/>

      <g class="offer-text">
        <text x="284" y="808" font-size="368" textLength="395" lengthAdjust="spacingAndGlyphs" fill="var(--depth)">50</text>
        <text x="300" y="796" font-size="368" textLength="395" lengthAdjust="spacingAndGlyphs" fill="url(#numeral-fill)">50</text>
      </g>

      <g class="percent-depth" fill="none" stroke="var(--depth)" stroke-width="24">
        <polygon points="783,461 806,461 646,821 623,821" fill="var(--depth)" stroke="none"/>
        <ellipse cx="721" cy="521" rx="28" ry="46"/>
        <ellipse cx="811" cy="573" rx="28" ry="46"/>
      </g>
      <g class="percent-sign" fill="none" stroke="url(#numeral-fill)" stroke-width="24">
        <polygon points="791,455 814,455 654,815 631,815" fill="var(--numeral)" stroke="none"/>
        <ellipse cx="729" cy="515" rx="28" ry="46" stroke="var(--numeral)"/>
        <ellipse cx="819" cy="567" rx="28" ry="46" stroke="var(--numeral)"/>
      </g>

      <g class="offer-text">
        <text x="713" y="795" font-size="128" textLength="180" lengthAdjust="spacingAndGlyphs" fill="var(--depth)">off</text>
        <text x="720" y="788" font-size="128" textLength="180" lengthAdjust="spacingAndGlyphs" fill="url(#gold-fill)">off</text>
      </g>
    </svg>
  </div>
</div>
</body>
</html>
```